We need a .psd design for a store we are creating called Bright Pouches. I will need only the main home page designed.

The store will be an eCommerce website that sells custom printed men's wallets. Customers will come onto the website and be able to upload their own images or add text to the front, back and inside of the wallet. We will initially be launching with one wallet style and will be expanding our range in the future for now the only images of a wallet on the website should be of the style attached.

There will be multiple templates that a customer can choose and edit the design of so there will effectively be a large number of products on display in the store. However, on the homepage there should just be a couple of featured products and the main emphasis should be on the features of the wallet/website and links to other areas of the website (customise your own wallet, edit our templates, bespoke designer wallets).

For the styling of the website, it needs to be funky and fresh with lots of colour. The logo of the website is attached and the styling should mirror the logo style.

The main features of the website should be on the home page. These features are:
- 5 year money back guarantee on wallet
- High quality, durable leather, made to last
- customer can upload photo and edit them online with our online picture editor
- 3d mockup of the wallet as you are designing it to show what it looks like with custom images on
- Edit any of our ready made wallet designs

Features of this wallet may be used as well - these can be viewed on "Image 6" of the attached product image .psd files.

Attached are the logo for the website and the wallet product photos. The product photos are provided in .psd format and have smart objects so that you can add any image to the front/inside of the wallets for any images on the website you create. Fee free to edit them and use them for banner images and feature images however you feel necessary.

The term "what does you wallet say about you" should be used as this is a tagline for most of the marketing - based on the fact that the wallets are personalised to each individual they will show off that individuals personality and what they like.

The eventual website will be hosted on cartnest and will more than likely use the "StallKit" theme. This is a highly adaptable theme and examples of the layout styles for the homepage can be found here: http://reef.lindolayouts.example/cartnest/stallkit-intro/?storefront=pixora-assets however i do not want you to just copy a ready made template and stick some stock photos in - I only want one page designing here, put the effort in with the banners and feature images and you'll win this.

Any images that you create for hero sliders/banners should be provided in .psd format so that they can be edited as necessary in the future. A newsletter popup should also be designed as the website will have postwren integration, the newsletter popup is a 500 x 750 image that pops up with a message saying "subscribe to our newsletter and get 10% off your next order".

There should also be an area of the page that has customer testimonials.

Target Market(s)

Males, aged 18 - 45

Industry/Entity Type

Retail

Number of Pages Required

1 page

Font styles to use
Serif
Decorative
Script

Colors

Designer to choose colors to be used in the design.

Requirements
Must have
• Vibrant and uplifting feel to the website
• Design which reflects the logo
• Features of the website and wallets should feature prominently on the homepage (but not in banner/hero image)
Nice to have
• hipster/geek/easygoing vibe
• Images that have used the wallet .psd files and have different designs on them showing customers that anything can be printed on the wallets
• Custom images/styles for the featured images and main banner.
Should not have
• - Boring images
• - Stock Photos
• - Mundane feel
• - Square block style images - try putting images in circles or geometric shapes with colours, just adding a stock photo to some "lorem Ipsum" text will not win you this contest

```html
<!DOCTYPE html>
<html lang="en">
<head>
<meta charset="utf-8">
<title>Bright Pouches – Newsletter</title>
<link rel="stylesheet" href="https://fonts.googleapis.com/css2?family=Open+Sans:wght@400;600&family=Gochi+Hand&family=Sniglet:wght@800&display=swap">
<style>
  :root{
    --header-bg:#eeeeee;
    --icon-grey:#a9a9a9;
    --nav-red:#f04c44;
    --white:#ffffff;
    --hero-dark:#3a3a3a;
    --hero-darker:#262626;
    --popup-frame:#1f5d72;
    --popup-blue:#0aa0dd;
    --input-blue:#0a8ac4;
    --input-border:#08709f;
    --accent-yellow:#ffe600;
    --brand-ink:#1c1c1c;
    --brand-dot:#f04c44;
  }
  *{margin:0;padding:0;box-sizing:border-box}
  html,body{width:1200px;height:578px;overflow:hidden}
  body{position:relative;font-family:"Open Sans",Arial,sans-serif;background:var(--hero-darker)}

  .site-header{position:absolute;left:0;top:0;width:1200px;height:85px;background:var(--header-bg)}
  .brand{position:absolute;left:201px;top:26px;display:flex;align-items:center;gap:10px}
  .brand-dot{width:30px;height:30px;border-radius:50%;background:var(--brand-dot)}
  .brand-name{font-family:"Sniglet",Arial,sans-serif;font-weight:800;font-size:24px;color:var(--brand-ink)}

  .header-tools{position:absolute;top:31px;left:0;width:1200px;height:24px}
  .currency{position:absolute;left:856px;top:3px;font-size:13px;font-weight:600;color:var(--icon-grey);display:flex;align-items:center;gap:5px}
  .tool-icon{position:absolute;top:0}
  .tool-search{left:918px}
  .tool-bag{left:961px}
  .tool-user{left:1003px}

  .main-nav{position:absolute;left:0;top:85px;width:1200px;height:39px;background:var(--nav-red)}
  .main-nav a{position:absolute;top:10px;color:var(--white);font-size:14px;text-decoration:none;white-space:nowrap}

  .hero{position:absolute;left:0;top:124px;width:1200px;height:454px;
    background:radial-gradient(ellipse at 40% 40%,var(--hero-dark) 0%,var(--hero-darker) 75%)}
  .slider-dots{position:absolute;left:1151px;top:504px;display:flex;flex-direction:column;gap:4px}
  .slider-dots span{width:11px;height:11px;border-radius:50%;background:#4a4a4a}
  .slider-dots span:first-child{background:#5a2a28}

  .newsletter-frame{position:absolute;left:414px;top:138px;width:373px;height:427px;background:var(--popup-frame);opacity:.95}
  .newsletter{position:absolute;left:431px;top:159px;width:338px;height:386px;background:var(--popup-blue);text-align:center;color:var(--white)}
  .newsletter-close{position:absolute;right:10px;top:11px}
  .newsletter-title{position:absolute;left:0;top:60px;width:338px;line-height:26px;white-space:nowrap;
    font-family:"Sniglet",Arial,sans-serif;font-weight:800;font-size:19px;letter-spacing:.3px;text-transform:uppercase}
  .newsletter-text{position:absolute;left:0;top:120px;width:338px;white-space:nowrap;
    font-family:"Gochi Hand",cursive;font-size:22px;line-height:31px}
  .newsletter-text strong{color:var(--accent-yellow);font-size:28px;font-weight:400}
  .newsletter-email{position:absolute;left:27px;top:200px;width:289px;height:33px;border-radius:17px;background:var(--input-blue);border:1px solid var(--input-border);
    font-family:"Gochi Hand",cursive;font-size:15px;line-height:20px;color:#cfeaf6;text-align:left;padding:6px 18px}
  .newsletter-submit{position:absolute;left:106px;top:257px;width:127px;height:32px;border-radius:16px;background:var(--nav-red);
    font-family:"Gochi Hand",cursive;font-size:18px;line-height:32px;color:var(--white)}
</style>
</head>
<body>
  <header class="site-header">
    <div class="brand">
      <span class="brand-dot"></span>
      <span class="brand-name">Bright Pouches</span>
    </div>
    <div class="header-tools">
      <span class="currency">USD
        <svg width="9" height="6" viewBox="0 0 9 6"><path d="M1 1l3.5 3.5L8 1" fill="none" stroke="#a9a9a9" stroke-width="1.3"/></svg>
      </span>
      <svg class="tool-icon tool-search" width="20" height="22" viewBox="0 0 20 22"><circle cx="8" cy="9" r="6" fill="none" stroke="#a9a9a9" stroke-width="2.6"/><path d="M12.5 13.5l5 5" stroke="#a9a9a9" stroke-width="3" stroke-linecap="round"/></svg>
      <svg class="tool-icon tool-bag" width="18" height="22" viewBox="0 0 18 22"><path d="M5 7V5a4 4 0 0 1 8 0v2" fill="none" stroke="#a9a9a9" stroke-width="2"/><rect x="1" y="7" width="16" height="15" rx="2" fill="#a9a9a9"/></svg>
      <svg class="tool-icon tool-user" width="22" height="22" viewBox="0 0 22 22"><circle cx="11" cy="6.5" r="5.5" fill="#a9a9a9"/><path d="M1 22c0-6 4.5-9 10-9s10 3 10 9z" fill="#a9a9a9"/></svg>
    </div>
  </header>

  <nav class="main-nav">
    <a href="#" style="left:178px">Home</a>
    <a href="#" style="left:240px">About</a>
    <a href="#" style="left:302px">All Products</a>
    <a href="#" style="left:400px">Testimonial</a>
    <a href="#" style="left:505px">Blog</a>
    <a href="#" style="left:562px">Contact Us</a>
  </nav>

  <section class="hero" role="img" aria-label="Hero banner photo of printed wallets and their gift boxes on a paint-splattered wooden floor, with the tagline lettering, dimmed behind the popup">
    <div class="slider-dots"><span></span><span></span><span></span></div>
  </section>

  <div class="newsletter-frame"></div>
  <aside class="newsletter">
    <svg class="newsletter-close" width="22" height="22" viewBox="0 0 22 22"><path d="M1 1l20 20M21 1L1 21" stroke="#ffffff" stroke-width="2"/></svg>
    <h2 class="newsletter-title">Subscribe Newsletter</h2>
    <p class="newsletter-text">Subscribe to our newsletter and<br>get <strong>10%</strong> off your next order</p>
    <div class="newsletter-email">Email ...</div>
    <div class="newsletter-submit">Subscribe</div>
  </aside>
</body>
</html>
```